Business card design needed

I have started a new business called Marlow Auto Electrical, although the words Marlow Auto Electrical will be used on signage and documents I actually want to market the business as MAE. The services I offer are Mobile Auto Electrical, Automotive Air Conditioning and Test And Tag. My business will be targetting the Mining Industry, Civil, Rail, Agricultural and Workshop Testing And Tagging. My auto electrical service ranges from fault finding to new vehicle and mine compliance fit outs. I have a very strong focus on quality workmanship. I will upload the logo I have designed and want to use I am happy for the logo colour to change but the design itself must stay the same. I want the design to have a modern, eye catching, energetic feel. As I am a passionate motorsport fan I am happy for this to also influence the design. I am happy for the front of the card to have only the emblem and logo design and the back to have all the info.

Industry/Entity Type

Electrical

Contact Information for Business Card

MAE Marlow Auto Electrical, Dale Penrick, Auto Electrician, Mobile No 0417263859

Requirements
Must have
• On the business card it is mandatory that the following license numbers are shown:

MVRL38462
VDA L071348
ABN 61 839 204 518

```html
<!DOCTYPE html>
<html lang="en">
<head>
<meta charset="utf-8">
<title>Marlow Auto Electrical – Business Card</title>
<link rel="stylesheet" href="https://fonts.googleapis.com/css2?family=Source+Sans+3:wght@400;700&display=swap">
<style>
  :root {
    --card-black: #000000;
    --accent-lime: #e4ff12;
    --text-white: #ffffff;
  }
  html, body {
    margin: 0;
    padding: 0;
    width: 1200px;
    height: 741px;
    overflow: hidden;
    background: var(--card-black);
  }
  .card {
    position: relative;
    width: 1200px;
    height: 741px;
    background: var(--card-black);
    font-family: "Source Sans 3", "Myriad Pro", Arial, sans-serif;
  }
  .accent-band {
    position: absolute;
    left: 0;
    width: 100%;
    height: 20px;
    background: var(--accent-lime);
  }
  .accent-band--top { top: 0; }
  .accent-band--bottom { bottom: 0; }
  .business-name {
    position: absolute;
    left: 0;
    width: 100%;
    top: 346px;
    margin: 0;
    text-align: center;
    font-weight: 700;
    font-size: 60px;
    line-height: 70px;
    color: var(--accent-lime);
  }
  .licence-list {
    position: absolute;
    left: 0;
    width: 100%;
    top: 636px;
    margin: 0;
    padding: 0;
    list-style: none;
    text-align: center;
    color: var(--text-white);
    font-weight: 400;
    font-size: 18px;
    line-height: 26px;
  }
</style>
</head>
<body>
  <main class="card">
    <div class="accent-band accent-band--top"></div>
    <h1 class="business-name">Marlow Auto Electrical</h1>
    <ul class="licence-list">
      <li>MVRL38462</li>
      <li>VDA L071348</li>
      <li>ABN 61 839 204 518</li>
    </ul>
    <div class="accent-band accent-band--bottom"></div>
  </main>
</body>
</html>
```